Flyer für Immobilienmaklerunternehmen
Zielgruppe
Wir sind ein Immobilienmaklerunternehmen in Bochum.
Wir lassen die Flyer in die Briefkästen verteilen.
Wir möchten Eigentümer erreichen und diese am Besten zur Kontaktaufnahme motivieren. Oder zumindest in Erinnerung bleiben.
Viele brauchen unsere Dienstleistungen nur zu einem bestimmten Zeitpunkt.
Unsere Zielgruppe sind meist ältere Eigentümer, die entweder aus Sorge, wegen privatem Stress, Unwissenheit oder Erlösmaximierung einen Makler beauftragen.
Wir würden gerne mit den Flyern diejenigen ansprechen, die Sorge haben und ggf. unwissend sind. Hierbei stellen wir uns einen Flyer vor, der auf der Vorderseite ein Bild mit 'unsicheren Zeiten' nutzt, um Aufmerksamkeit zu erregen (wir haben bspw. einen Flyer mit einem Leuchtturm gesehen, der durch den Sturm den Weg weist, mit dem Spruch' Wir geben Ihnen auch in stürmischen Zeiten eine sichere Orientierung' etwas Ähnliches stellen wir uns vor) mit einem passenden Slogan.
Zudem hätten wir auf der Vorderseite ebenso unser Logo, als auch das Zertifikat.
Auf der Rückseite gerne die Motivation zur Kontaktaufnahme wie oben beschrieben, zudem hatten wir uns eine kurze Vorstellung unserer Dienstleistungen (Verkauf, Wertgutachten, Vermietung, Wohnflächenberechnung und Energieausweis) vorgestellt.
Dann hätten wir entweder gerne ein Teamfoto eingebaut mit Einladung zur Kontaktaufnahme, alternativ unseren Slogan 'Unser Erstgespräch kostet Sie einen Kaffee und einen Keks.' und anstelle des Teamfotos dann einem Bild von Kaffee und Keksen o.Ä.
Die Adressdaten der Firmen bitte sehr dezent/klein plazieren.
Bitte diese beiden Büros einbauen:
Lanberg Immobilien
Molvener Weg 417
44861 Bochum
www.lanberg-immobilien-beispiel.info
und
Kesu Immobilien
Tillweg 27
44627 Herne
www.kesu-beispiel.de
(Bitte die Logos von der Homepage verwenden)
Aufgabenstellung
Unser Logo sollte zu finden sein, sowie die Geschäftsfarben (aus dem Logo)
Zudem muss die Handhabbarkeit beim Verteilen gegeben sein.
Wir kennen uns nicht so gut aus und benötigen am Schluss ein Ergebnis, mit dem wir die Flyer direkt drucken lassen können.
Bei Spezialformaten freuen wir uns, wenn Sie uns sagen, wo man diese drucken lassen kann.

```html
<!DOCTYPE html>
<html lang="de">
<head>
<meta charset="utf-8">
<title>Flyer Lanberg Immobilien – Vorder- und Rückseite</title>
<link rel="stylesheet" href="https://fonts.googleapis.com/css2?family=Oswald:wght@300;400;500;600&display=swap">
<style>
  :root {
    --brand-green: #8cc63f;
    --ink-dark: #3b403b;
    --paper-white: #f2f2f0;
    --stage: #e4e7e2;
    --photo-dark: #4b5552;
    --photo-mid: #6f7a74;
    --photo-light: #9aa19b;
    --badge-grey: #8a8c8b;
  }
  * { box-sizing: border-box; margin: 0; padding: 0; }
  html, body {
    width: 1200px; height: 900px; overflow: hidden;
    background: var(--stage);
    font-family: "Oswald", "Arial Narrow", sans-serif;
  }
  .flyer-set {
    position: absolute; left: 20px; top: 50px;
    display: flex; gap: 28px;
  }
  .page {
    position: relative; width: 566px; height: 800px; overflow: hidden;
    box-shadow: 0 6px 18px rgba(0,0,0,0.12);
  }

  /* Front side */
  .front { background: var(--photo-dark); }
  .front-photo {
    position: absolute; inset: 0;
    background: linear-gradient(180deg, var(--photo-dark) 0%, var(--photo-mid) 45%, var(--photo-light) 75%, var(--photo-mid) 100%);
  }
  .front-shapes { position: absolute; inset: 0; }
  .quote-mark {
    position: absolute; left: 164px; top: 74px;
    font-family: Georgia, serif; font-weight: 700; font-size: 140px; line-height: 1;
    color: #fff;
  }
  .slogan {
    position: absolute; left: 256px; top: 110px;
    color: #fff; line-height: 1;
  }
  .slogan-lead {
    display: block; color: var(--brand-green);
    font-size: 90px; font-weight: 500; letter-spacing: -2px;
  }
  .slogan-rest {
    display: block; font-size: 44px; font-weight: 500; margin-top: 16px; letter-spacing: -0.5px;
  }
  .slogan-rest + .slogan-rest { margin-top: 10px; }
  .accent { color: var(--brand-green); }
  .certificate {
    position: absolute; left: 441px; top: 410px; width: 90px; height: 176px;
  }
  .brand-block {
    position: absolute; left: 40px; top: 628px;
    display: flex; align-items: center; gap: 10px;
  }
  .brand-square { width: 16px; height: 16px; background: var(--brand-green); }
  .brand-name {
    font-size: 22px; font-weight: 400; color: var(--brand-green); line-height: 1;
  }
  .brand-web {
    position: absolute; left: 40px; top: 742px; width: 200px;
    font-size: 13.5px; font-weight: 500; color: var(--brand-green); white-space: nowrap;
  }
  .call-note {
    position: absolute; left: 308px; top: 678px; width: 240px;
    font-size: 14px; font-weight: 300; color: #fff; line-height: 1.35;
  }
  .call-number {
    position: absolute; left: 280px; top: 736px;
    display: flex; align-items: center; gap: 8px;
    font-size: 21px; font-weight: 500; color: #fff;
  }

  /* Back side */
  .back { background: var(--brand-green); }
  .back-shapes { position: absolute; inset: 0; }
  .back-title {
    position: absolute; left: 59px; top: 46px;
    font-size: 50px; font-weight: 500; line-height: 1.08; color: var(--ink-dark);
  }
  .service { position: absolute; width: 150px; color: var(--ink-dark); }
  .service svg { display: block; width: 34px; height: 38px; }
  .service-name {
    font-size: 22px; font-weight: 500; margin-top: 10px; line-height: 1.1; white-space: nowrap;
  }
  .service-text {
    font-size: 9.5px; font-weight: 300; line-height: 1.4; margin-top: 10px; color: #4b524a;
  }
  .service-divider {
    position: absolute; left: 59px; top: 371px; width: 451px; height: 1px;
    background: rgba(255,255,255,0.55);
  }
  .team-photo {
    position: absolute; left: 0; top: 648px; width: 318px; height: 152px;
    background: linear-gradient(90deg, #d9d9d6 0%, #3a3a3a 30%, #f0f0ee 50%, #2f2f2f 75%, #e8e8e6 100%);
    opacity: 0.85;
  }
  .contact-invite {
    position: absolute; left: 346px; top: 648px;
    font-size: 24px; font-weight: 500; line-height: 1.2; color: var(--brand-green);
  }
  .office {
    position: absolute; top: 720px; font-style: normal;
    font-size: 9.5px; font-weight: 300; line-height: 1.4; color: var(--ink-dark);
  }
  .office .office-web { color: var(--brand-green); }
</style>
</head>
<body>
<main class="flyer-set">

  <!-- Front side -->
  <section class="page front">
    <div class="front-photo" role="img" aria-label="Foto: Wegweiser mit vielen Richtungsschildern auf einer rissigen Straße unter dunklem, stürmischem Himmel"></div>
    <svg class="front-shapes" viewBox="0 0 566 800" aria-hidden="true">
      <polygon points="0,594 256,536 256,800 0,800" fill="var(--paper-white)"/>
      <polygon points="256,536 566,468 566,800 256,800" fill="var(--brand-green)"/>
    </svg>
    <div class="quote-mark">“</div>
    <h1 class="slogan">
      <span class="slogan-lead">Mit uns</span>
      <span class="slogan-rest">finden Sie den</span>
      <span class="slogan-rest"><span class="accent">richtigen</span> Weg.</span>
    </h1>
    <svg class="certificate" viewBox="0 0 90 176" role="img" aria-label="Zertifikatssiegel">
      <path d="M0,8 Q0,0 8,0 H82 Q90,0 90,8 V136 Q90,176 45,176 Q0,176 0,136 Z" fill="var(--badge-grey)"/>
    </svg>
    <div class="brand-block">
      <span class="brand-square"></span>
      <span class="brand-name">Lanberg Immobilien</span>
    </div>
    <div class="brand-web">lanberg-immobilien-beispiel.info</div>
    <p class="call-note">Rufen Sie uns an. Wir freuen uns auf ein persönliches Gespräch.</p>
    <div class="call-number">
      <svg width="20" height="20" viewBox="0 0 24 24" aria-hidden="true"><path fill="#fff" d="M6.6 10.8a15.1 15.1 0 0 0 6.6 6.6l2.2-2.2a1 1 0 0 1 1-.25 11.4 11.4 0 0 0 3.6.57 1 1 0 0 1 1 1V20a1 1 0 0 1-1 1A17 17 0 0 1 3 4a1 1 0 0 1 1-1h3.5a1 1 0 0 1 1 1c0 1.250.2 2.450.57 3.57a1 1 0 0 1-.25 1z"/></svg>
      <span>02 34 - 55 48 21 07</span>
    </div>
  </section>

  <!-- Back side -->
  <section class="page back">
    <svg class="back-shapes" viewBox="0 0 566 800" aria-hidden="true">
      <polygon points="0,644 566,527 566,800 0,800" fill="var(--paper-white)"/>
    </svg>
    <h2 class="back-title">Unsere<br>Dienstleistungen</h2>

    <article class="service" style="left:59px; top:190px;">
      <svg viewBox="0 0 34 38" fill="none" stroke="var(--ink-dark)" stroke-width="2" aria-hidden="true"><path d="M3 17 L17 4 L31 17 V35 H3 Z"/><rect x="13" y="25" width="8" height="10"/></svg>
      <h3 class="service-name">Verkauf</h3>
      <p class="service-text">Verkaufen Sie Ihre Immobilie in nur sechs Schritten – von der Besichtigung bis zum Notartermin.</p>
    </article>
    <article class="service" style="left:212px; top:190px;">
      <svg viewBox="0 0 34 38" fill="none" stroke="var(--ink-dark)" stroke-width="2" aria-hidden="true"><path d="M17 3 L31 8 V19 Q31 30 17 36 Q3 30 3 19 V8 Z"/><path d="M11 19 L15.5 23.5 L23 14"/></svg>
      <h3 class="service-name">Wertgutachten</h3>
      <p class="service-text">Wir ermitteln den Wert Ihrer Immobilie – sie können zwischen unterschiedlichen Arten wählen.</p>
    </article>
    <article class="service" style="left:362px; top:190px;">
      <svg viewBox="0 0 34 38" fill="none" stroke="var(--ink-dark)" stroke-width="2" aria-hidden="true"><circle cx="23" cy="12" r="8"/><circle cx="25" cy="10" r="2"/><path d="M17 18 L4 31 M8 27 L12 31 M5 30 L8 33"/></svg>
      <h3 class="service-name">Vermietung</h3>
      <p class="service-text">Wir helfen Ihnen, Ihre Immobilie Ihren Wünschen entsprechend zu vermieten. Wir prüfen – Sie wählen aus!</p>
    </article>

    <div class="service-divider"></div>

    <article class="service" style="left:59px; top:405px; width:200px;">
      <svg viewBox="0 0 34 38" fill="none" stroke="var(--ink-dark)" stroke-width="2" aria-hidden="true"><rect x="3" y="2" width="28" height="34" rx="3"/><rect x="8" y="7" width="18" height="6"/><g stroke-width="1.6"><circle cx="10" cy="19" r="1.6"/><circle cx="17" cy="19" r="1.6"/><circle cx="24" cy="19" r="1.6"/><circle cx="10" cy="25" r="1.6"/><circle cx="17" cy="25" r="1.6"/><circle cx="24" cy="25" r="1.6"/><circle cx="10" cy="31" r="1.6"/><circle cx="17" cy="31" r="1.6"/><circle cx="24" cy="31" r="1.6"/></g></svg>
      <h3 class="service-name">Wohnflächenberechnung</h3>
      <p class="service-text">Wir erstellen zeitnah eine korrekte Wohnflächenberechnung nach Wohnflächenverordnung.</p>
    </article>
    <article class="service" style="left:282px; top:405px; width:170px;">
      <svg viewBox="0 0 34 38" fill="none" stroke="var(--ink-dark)" stroke-width="2" aria-hidden="true"><path d="M6 2 H28 V28 L22 35 H6 Z"/><path d="M22 35 V28 H28"/><path d="M11 10 H23 M11 16 H23 M11 22 H19"/></svg>
      <h3 class="service-name">Energieausweis</h3>
      <p class="service-text">In Kooperation kümmern wir uns zeitnah um die Erstellung Ihres Energieausweises.</p>
    </article>

    <div class="team-photo" role="img" aria-label="Teamfoto: fünf Mitarbeiterinnen und Mitarbeiter in Schwarz und Weiß vor hellem Hintergrund"></div>
    <h3 class="contact-invite">Zögern Sie nicht uns<br>zu kontaktieren!</h3>
    <address class="office" style="left:346px;">
      Lanberg Immobilien<br>Molvener Weg 417<br>44861 Bochum<br>0234 / 55482107<br><span class="office-web">lanberg-immobilien-beispiel.info</span>
    </address>
    <address class="office" style="left:474px;">
      Kesu Immobilien<br>Tillweg 27<br>44627 Herne<br>02325 / 61408<br><span class="office-web">kesu-beispiel.de</span>
    </address>
  </section>

</main>
</body>
</html>
```